Brightwave MolarNet IT Inc. new website

i need a website for my company which is dedicated to installation and service of computer systems in Dental Offices. I would like for it to encompass a technology feel and professional look. The company deals with all aspects of technology like, Audio Visual, computer systems and networks, Cloud services like data backup, data center. We provide manage services, support and services to Dental Professionals.
Updates

Looking for a Technology font but professional look Added Wednesday, April 20, 2016

Target Market(s)

Dental, Dentist

Industry/Entity Type

Dental

Number of Pages Required

5+ page

Font styles to use
Other font styles liked:
• Futuristic or Techy

Colors
0255a3
ec1f27

Requirements
Must have
• Tabs
Nice to have
• Have no idea maybe some suggestion on your part may help
Should not have
• A professional feel but have a techy look

Files

```html
<!DOCTYPE html>
<html lang="en">
<head>
<meta charset="utf-8">
<title>Brightwave MolarNet IT Inc.</title>
<link rel="stylesheet" href="https://fonts.googleapis.com/css2?family=Lato:wght@400;700&family=Open+Sans:wght@400;600&display=swap">
<style>
:root{
  --brand:#0255a3;
  --brand-bright:#2f7fd6;
  --brand-dark:#0a4a94;
  --accent:#d1121b;
  --ink:#333;
  --muted:#555;
  --light-bg:#f2f2f2;
  --rule:#dcdcdc;
  --footer:#2e2e2e;
  --footer-bottom:#1f1f1f;
  --white:#fff;
}
*{margin:0;padding:0;box-sizing:border-box}
html,body{width:1200px;height:2375px;overflow:hidden}
body{position:relative;background:var(--white);font-family:"Open Sans",Arial,sans-serif;color:var(--ink)}
.abs{position:absolute}
.heading{font-family:"Lato",Arial,sans-serif;font-weight:700;color:var(--brand);text-transform:uppercase}

/* header */
.site-header{left:0;top:0;width:1200px;height:124px;border-top:3px solid var(--brand);background:var(--white)}
.brand{left:131px;top:38px;display:flex;align-items:center;gap:10px;font-family:"Lato",sans-serif;font-weight:700;font-size:22px;color:var(--brand)}
.brand-mark{width:30px;height:30px;background:var(--brand)}
.main-nav{left:516px;top:50px;display:flex;gap:0;font-family:"Open Sans",sans-serif;font-size:13px;color:#333}
.main-nav span{position:absolute;white-space:nowrap}
.main-nav .active{color:var(--brand)}

/* hero */
.hero{left:0;top:124px;width:1200px;height:435px;background:linear-gradient(90deg,#4a4a4a 0%,#6f6f6f 35%,#5a5d62 60%,#2b2e33 100%)}
.hero-title{left:0;top:252px;width:1200px;text-align:center;font-family:"Lato",sans-serif;font-weight:700;font-size:30px;color:var(--white)}
.hero-sub{left:0;top:309px;width:1200px;text-align:center;font-size:15px;color:var(--white)}
.btn-quote{left:521px;top:356px;width:158px;height:51px;background:var(--accent);color:var(--white);font-size:14px;display:flex;align-items:center;justify-content:center;border-radius:2px}
.dot{width:9px;height:9px;border-radius:50%;background:#bbb;top:496px}
.dot.on{background:var(--white)}

/* features */
.features{left:0;top:559px;width:1200px;height:305px;display:flex}
.feature{position:relative;width:400px;height:305px;text-align:center;color:var(--white)}
.feature:nth-child(1){background:radial-gradient(circle at 60% 40%,#1e6fcf,#0b4fa5)}
.feature:nth-child(2){width:400px;background:radial-gradient(circle at 50% 40%,#3b86d8,#1c62bd)}
.feature:nth-child(3){background:radial-gradient(circle at 50% 40%,#4b94e0,#2466c0)}
.feature-icon{position:absolute;left:154px;top:39px;width:92px;height:92px;border-radius:50%;background:var(--white);display:flex;align-items:center;justify-content:center}
.feature h3{position:absolute;top:164px;width:100%;font-family:"Lato",sans-serif;font-size:20px;font-weight:700}
.feature p{position:absolute;left:22px;top:208px;width:356px;font-size:11px;line-height:19px;text-align:justify;text-align-last:center}
.features-shadow{left:100px;top:864px;width:1000px;height:40px;background:radial-gradient(ellipse at 50% 0%,rgba(0,0,0,.18),rgba(0,0,0,0) 70%)}

/* welcome */
.welcome-title{left:0;top:940px;width:1200px;text-align:center;font-size:29px}
.welcome-text{left:131px;top:1000px;width:938px;font-size:11px;line-height:19px;text-align:center}
.btn-more{left:549px;top:1089px;width:102px;height:40px;background:var(--brand);color:var(--white);font-size:11px;display:flex;align-items:center;justify-content:center;border-radius:2px}

/* services */
.services{left:0;top:1183px;width:1200px;height:484px;background:var(--light-bg);border-top:2px solid var(--rule);border-bottom:2px solid var(--rule)}
.services-title{left:0;top:1237px;width:1200px;text-align:center;font-size:29px}
.service{position:absolute;top:1319px;width:213px}
.service-photo{width:213px;height:117px;border:4px solid var(--white);box-shadow:0 1px 4px rgba(0,0,0,.25)}
.service h4{margin-top:20px;font-size:20px}
.service p{margin-top:10px;font-size:11px;line-height:19px;color:var(--muted);text-align:justify}
.read-link{display:block;margin-top:16px;font-size:11px;color:var(--brand)}

/* news & testimonials */
.section-title{font-size:29px}
.news-item{position:absolute;left:131px;width:400px}
.news-photo{position:absolute;left:0;top:0;width:135px;height:98px;border:3px solid var(--white);box-shadow:0 1px 4px rgba(0,0,0,.3)}
.news-date{position:absolute;left:157px;top:4px;font-size:11px;color:#444}
.news-headline{position:absolute;left:157px;top:30px;font-family:"Lato",sans-serif;font-weight:700;font-size:15px;line-height:24px;color:var(--brand);text-transform:uppercase}
.col-divider{left:553px;top:1702px;width:2px;height:293px;background:var(--rule)}
.testimonial-text{left:628px;top:1786px;width:442px;font-size:11px;line-height:19px;color:var(--muted);text-align:justify}
.testimonial-text p+p{margin-top:19px}
.author{left:632px;top:1922px;font-size:13px;font-style:italic;color:var(--brand)}
.author-role{left:628px;top:1944px;font-size:12px;color:#444}

/* footer */
.site-footer{left:0;top:2058px;width:1200px;height:247px;background:var(--footer);border-top:5px solid var(--brand)}
.footer-bottom{left:0;top:2305px;width:1200px;height:70px;background:var(--footer-bottom);color:#ddd;font-size:12px;display:flex;align-items:center;justify-content:center}
.footer-heading{top:2106px;font-family:"Lato",sans-serif;font-weight:700;font-size:15px;color:var(--white);text-transform:uppercase}
.quick-links{left:134px;top:2148px;list-style:none;font-size:11px;line-height:19px;color:var(--white)}
.contact-line{left:325px;display:flex;align-items:flex-start;gap:14px;font-size:11px;line-height:15px;color:var(--white)}
.contact-line svg{flex:none}
.newsletter-note{left:589px;top:2150px;font-size:11px;color:#ddd}
.email-field{left:589px;top:2183px;width:195px;height:33px;background:#555;color:#eee;font-size:10px;padding:10px 0 0 10px}
.btn-subscribe{left:589px;top:2230px;width:84px;height:27px;background:var(--brand);color:var(--white);font-size:10px;display:flex;align-items:center;justify-content:center}
.footer-brand{left:880px;top:2120px;display:flex;align-items:center;gap:10px;font-family:"Lato",sans-serif;font-weight:700;font-size:20px;color:#bdbdbd}
.footer-brand .brand-mark{background:#bdbdbd;width:26px;height:26px}
.social{width:34px;height:34px;border:2px solid var(--white);border-radius:50%;top:2194px}
</style>
</head>
<body>

<header class="site-header abs">
  <div class="brand abs"><span class="brand-mark"></span>Brightwave MolarNet IT</div>
  <nav class="main-nav abs">
    <span class="active" style="left:0">HOME</span>
    <span style="left:81px">ABOUT US</span>
    <span style="left:185px">SERVICES</span>
    <span style="left:285px">TECHNOLOGY</span>
    <span style="left:415px">CONTACT US</span>
    <svg style="position:absolute;left:540px;top:3px" width="12" height="12" viewBox="0 0 12 12"><circle cx="5" cy="5" r="3.6" fill="none" stroke="#0255a3" stroke-width="1.8"/><line x1="7.6" y1="7.6" x2="11" y2="11" stroke="#0255a3" stroke-width="2"/></svg>
  </nav>
</header>

<section class="hero abs" role="img" aria-label="Photo of a dental professional viewing dental X-ray scans on a monitor"></section>
<h1 class="hero-title abs">INSTALLATION AND SERVICE</h1>
<p class="hero-sub abs">Audio Visual, computer systems and networks, Cloud services of data backup</p>
<div class="btn-quote abs">REQUEST QUOTE</div>
<span class="dot abs" style="left:571px"></span>
<span class="dot abs on" style="left:594px"></span>
<span class="dot abs" style="left:620px"></span>

<section class="features abs">
  <div class="feature">
    <div class="feature-icon"><svg width="44" height="40" viewBox="0 0 44 40"><rect x="3" y="3" width="38" height="25" rx="2" fill="#222"/><rect x="7" y="7" width="30" height="17" fill="#fff"/><rect x="18" y="28" width="8" height="6" fill="#222"/><rect x="12" y="34" width="20" height="3" fill="#222"/></svg></div>
    <h3>MANAGE</h3>
    <p>Nemo enim ipsam voluptatem quia voluptas sit aspernatur aut odit aut fugit, sed quia consequuntur magni dolores eos qui ratione voluptatem sequi nesciunt.</p>
  </div>
  <div class="feature">
    <div class="feature-icon"><svg width="44" height="44" viewBox="0 0 44 44"><circle cx="22" cy="22" r="18" fill="none" stroke="#222" stroke-width="5"/><circle cx="22" cy="22" r="8" fill="none" stroke="#222" stroke-width="4"/><g stroke="#222" stroke-width="6"><line x1="9" y1="9" x2="16" y2="16"/><line x1="35" y1="9" x2="28" y2="16"/><line x1="9" y1="35" x2="16" y2="28"/><line x1="35" y1="35" x2="28" y2="28"/></g></svg></div>
    <h3>SUPPORT</h3>
    <p>Nemo enim ipsam voluptatem quia voluptas sit aspernatur aut odit aut fugit, sed quia consequuntur magni dolores eos qui ratione voluptatem sequi nesciunt.</p>
  </div>
  <div class="feature">
    <div class="feature-icon"><svg width="36" height="44" viewBox="0 0 36 44"><rect x="4" y="4" width="28" height="38" fill="none" stroke="#222" stroke-width="3"/><g fill="#222"><rect x="9" y="10" width="5" height="5"/><rect x="22" y="10" width="5" height="5"/><rect x="9" y="19" width="5" height="5"/><rect x="22" y="19" width="5" height="5"/><rect x="14" y="31" width="8" height="11"/><rect x="15" y="8" width="6" height="2"/><rect x="17" y="6" width="2" height="6"/></g></svg></div>
    <h3>SERVICE</h3>
    <p>Nemo enim ipsam voluptatem quia voluptas sit aspernatur aut odit aut fugit, sed quia consequuntur magni dolores eos qui ratione voluptatem sequi nesciunt.</p>
  </div>
</section>
<div class="features-shadow abs"></div>

<h2 class="welcome-title heading abs">WELCOME TO BRIGHTWAVE MOLARNET IT</h2>
<p class="welcome-text abs">Nemo enim ipsam voluptatem quia voluptas sit aspernatur aut odit aut fugit, sed quia consequuntur magni dolores eos qui ratione voluptatem sequi nesciunt. Neque porro quisquam est, qui dolorem ipsum quia dolor sit amet, consectetur, adipisci velit, sed quia non numquam eius modi tempora incidunt ut labore et dolore magnam aliquam quaerat voluptatem.At vero eos et accusamus et iusto odio dignissimos ducimus qui blanditiis praesentium voluptatum deleniti atque corrupti quos dolores et quas</p>
<div class="btn-more abs">Read More</div>

<section class="services abs"></section>
<h2 class="services-title heading abs">OUR SERVICES</h2>
<article class="service" style="left:131px">
  <div class="service-photo" role="img" aria-label="Photo of a dental treatment room with a chair and monitors" style="background:linear-gradient(135deg,#cfe0f2,#3f73b8)"></div>
  <h4 class="heading">AUDIO VISUAL</h4>
  <p>Neque porro quisquam est, qui dolorem ipsum quia dolor sit amet, consectetur, adipisci velit, sed quia</p>
  <span class="read-link">Read More &raquo;</span>
</article>
<article class="service" style="left:369px">
  <div class="service-photo" role="img" aria-label="Photo of two dentists reviewing an X-ray on a screen" style="background:linear-gradient(135deg,#e7ecef,#7a8fa3)"></div>
  <h4 class="heading">NETWORKING</h4>
  <p>Neque porro quisquam est, qui dolorem ipsum quia dolor sit amet, consectetur, adipisci velit, sed quia</p>
  <span class="read-link">Read More &raquo;</span>
</article>
<article class="service" style="left:609px">
  <div class="service-photo" role="img" aria-label="Photo of a dental team working at computers" style="background:linear-gradient(135deg,#f1f4f7,#9fb3c6)"></div>
  <h4 class="heading">CLOUD SERVICES</h4>
  <p>Neque porro quisquam est, qui dolorem ipsum quia dolor sit amet, consectetur, adipisci velit, sed quia</p>
  <span class="read-link">Read More &raquo;</span>
</article>
<article class="service" style="left:850px">
  <div class="service-photo" role="img" aria-label="Photo of a patient looking at dental images on a monitor" style="background:linear-gradient(135deg,#e9e2dc,#5d5a58)"></div>
  <h4 class="heading">DATA BACKUP</h4>
  <p>Neque porro quisquam est, qui dolorem ipsum quia dolor sit amet, consectetur, adipisci velit, sed quia</p>
  <span class="read-link">Read More &raquo;</span>
</article>

<h2 class="section-title heading abs" style="left:131px;top:1711px">RECENT NEWS</h2>
<article class="news-item" style="top:1784px">
  <div class="news-photo" role="img" aria-label="Photo of a dental treatment room" style="background:linear-gradient(135deg,#e4edf4,#8ea9c2)"></div>
  <span class="news-date">APR 19,2016</span>
  <h4 class="news-headline">Nemo enim ipsam voluptatem<br>&nbsp;quia voluptas</h4>
</article>
<article class="news-item" style="top:1906px">
  <div class="news-photo" role="img" aria-label="Photo of a dentist in a clinic" style="background:linear-gradient(135deg,#eef2f4,#9aaab5)"></div>
  <span class="news-date">APR 19,2016</span>
  <h4 class="news-headline">Nemo enim ipsam voluptatem<br>&nbsp;quia voluptas</h4>
</article>

<div class="col-divider abs"></div>
<h2 class="section-title heading abs" style="left:575px;top:1711px">TESTIMONIALS</h2>
<svg class="abs" style="left:1033px;top:1723px" width="40" height="18" viewBox="0 0 40 18"><polyline points="9,2 3,9 9,16" fill="none" stroke="#444" stroke-width="1.6"/><polyline points="31,2 37,9 31,16" fill="none" stroke="#444" stroke-width="1.6"/></svg>
<svg class="abs" style="left:579px;top:1786px" width="36" height="30" viewBox="0 0 36 30"><g fill="#999"><path d="M0 14 Q0 2 12 0 L13 4 Q6 6 6 12 L15 12 L15 30 L0 30Z"/><path d="M20 14 Q20 2 32 0 L33 4 Q26 6 26 12 L35 12 L35 30 L20 30Z"/></g></svg>
<div class="testimonial-text abs">
  <p>Nemo enim ipsam voluptatem quia voluptas sit aspernatur aut odit aut fugit, sed quia consequuntur magni dolores eos qui ratione voluptatem sequi nesciunt.</p>
  <p>Neque porro quisquam est, qui dolorem ipsum quia dolor sit amet, consectetur, adipisci velit, sed quia non numquam eius modi tempora incidunt ut labore et dolore magnam aliquam quaerat voluptatem.</p>
</div>
<span class="author abs">- Jane Rowan -</span>
<span class="author-role abs">Dentist of Hospital name</span>

<footer class="site-footer abs"></footer>
<h5 class="footer-heading abs" style="left:131px">QUICK LINKS</h5>
<ul class="quick-links abs"><li>Home</li><li>About us</li><li>Services</li><li>Technology</li><li>Contact us</li></ul>

<h5 class="footer-heading abs" style="left:325px">CONTACT US</h5>
<div class="contact-line abs" style="top:2151px"><svg width="13" height="12" viewBox="0 0 13 12"><path d="M1 4 Q6.5 0 12 4 L10 6 L8.5 4.5 L4.5 4.5 L3 6Z" fill="#fff"/><rect x="3" y="6" width="7" height="5" fill="#fff"/></svg>1 555 010 4827</div>
<div class="contact-line abs" style="top:2177px"><svg width="13" height="12" viewBox="0 0 13 12"><rect x="3" y="0" width="7" height="4" fill="#fff"/><rect x="0" y="4" width="13" height="5" fill="#fff"/><rect x="3" y="8" width="7" height="4" fill="#fff"/></svg>+44 20 7946 0321</div>
<div class="contact-line abs" style="top:2204px"><svg width="13" height="10" viewBox="0 0 13 10"><rect x="0.5" y="0.5" width="12" height="9" fill="none" stroke="#fff"/><polyline points="0.5,0.5 6.5,5.5 12.5,0.5" fill="none" stroke="#fff"/></svg><span style="text-decoration:underline">info@brightwavemolarnet.example</span></div>
<div class="contact-line abs" style="top:2231px"><svg width="13" height="14" viewBox="0 0 13 14"><path d="M6.5 14 L2 7 A5 5 0 1 1 11 7Z" fill="#fff"/><circle cx="6.5" cy="5" r="2" fill="#2e2e2e"/></svg><span>#2868 Lorem ipsum dolor sit amet,<br>consectetur adipiscing elit</span></div>

<h5 class="footer-heading abs" style="left:589px">NEWSLETTER</h5>
<p class="newsletter-note abs">Sign Up for Our Newsletter &amp; Promotion</p>
<div class="email-field abs">Enter Your email Id</div>
<div class="btn-subscribe abs">SUBSCRIBE</div>

<div class="footer-brand abs"><span class="brand-mark"></span>Brightwave MolarNet IT</div>
<span class="social abs" style="left:914px"></span>
<span class="social abs" style="left:953px"></span>
<span class="social abs" style="left:993px"></span>
<span class="social abs" style="left:1033px"></span>

<div class="footer-bottom abs">© 2016 Brightwave MolarNet IT. All Rights Reserved</div>

</body>
</html>
```